business card for a massage therapy practice named 'Meadow and Willow Massage Studio'

I really need a trendy, yet easy on the eyes business card to complement my logo. Ideally with some gold or rose gold foil work.

My uploaded file of the logo I have in horizontal but I have a vertical version as well. Another color that is used in the website is a blush pink here and there. I'd like to see some trendy tropical leaves in the design.

```html
<!DOCTYPE html>
<html lang="en">
<head>
<meta charset="utf-8">
<title>Meadow and Willow Massage Studio – Business Card</title>
<link href="https://fonts.googleapis.com/css2?family=Montserrat:wght@400;500;600&family=Kaushan+Script&display=swap" rel="stylesheet">
<style>
  :root {
    --backdrop: #6e6e6f;
    --card-black: #1f1f20;
    --card-white: #ffffff;
    --rose-gold: #e3a08e;
    --rose-gold-deep: #c97f6d;
    --gold: #a88c58;
    --ink: #161616;
    --mint: #7fd3c0;
  }
  * { box-sizing: border-box; margin: 0; padding: 0; }
  html, body { width: 865px; height: 1200px; overflow: hidden; }
  body {
    background: var(--backdrop);
    font-family: "Montserrat", Arial, sans-serif;
    position: relative;
  }
  .card {
    position: absolute;
    left: 112px;
    width: 640px;
    height: 366px;
    overflow: hidden;
  }
  .card--back { top: 180px; background: var(--card-black); }
  .card--front { top: 630px; background: var(--card-white); }

  .brand {
    position: absolute;
    display: flex;
    align-items: center;
    gap: 18px;
  }
  .brand__mark {
    width: 46px; height: 46px;
    border-radius: 50%;
    flex: none;
  }
  .brand__name {
    font-family: "Montserrat", Arial, sans-serif;
    font-weight: 500;
    font-size: 25px;
    line-height: 1.25;
    letter-spacing: 0.02em;
  }
  .card--back .brand { left: 150px; top: 140px; }
  .card--back .brand__mark { background: var(--rose-gold); }
  .card--back .brand__name { color: var(--rose-gold); }

  .card--front .brand { left: 70px; top: 62px; }
  .card--front .brand__mark { background: var(--gold); }
  .card--front .brand__name { color: var(--ink); }

  .foil-motif {
    position: absolute;
    right: 0; top: 40px;
    width: 150px; height: 326px;
    background: linear-gradient(160deg, #f3c3b4 0%, var(--rose-gold) 45%, var(--rose-gold-deep) 100%);
    border-top-left-radius: 75px;
  }

  .contact {
    position: absolute;
    left: 70px;
    top: 190px;
    width: 400px;
    text-align: center;
    color: var(--ink);
  }
  .contact__person {
    font-family: "Kaushan Script", cursive;
    font-size: 30px;
    margin-bottom: 10px;
  }
  .contact__line {
    font-size: 12px;
    line-height: 1.75;
  }
  .contact__line--small { font-size: 11px; }
</style>
</head>
<body>

  <section class="card card--back">
    <div class="brand">
      <span class="brand__mark"></span>
      <p class="brand__name">Meadow and Willow<br>Massage Studio</p>
    </div>
  </section>

  <section class="card card--front">
    <div class="brand">
      <span class="brand__mark"></span>
      <p class="brand__name">Meadow and Willow<br>Massage Studio</p>
    </div>

    <div class="contact">
      <p class="contact__person">Daniel Moon</p>
      <p class="contact__line">+822-5310-4478</p>
      <p class="contact__line">info@meadowandwillow.com | www.meadowandwillow.com</p>
      <p class="contact__line contact__line--small">6/F, Linden Tower, 218 Hanbit-ro, Gangnam-gu, Seoul, 06120 Korea</p>
    </div>

    <div class="foil-motif" role="img" aria-label="Large rose gold foil decorative motif along the right edge"></div>
  </section>

</body>
</html>
```